Business Card Design Project

We need a buisness card for a new digital sinage company. Our target cliants are small to mediaum buisness who want to advertise on out digital sinage network

Target Market(s)

Small to medium buisness

Industry/Entity Type

Digital

Requirements
Must have
• Must have logo

```html
<!DOCTYPE html>
<html lang="en">
<head>
<meta charset="utf-8">
<title>Vizo Business Cards</title>
<link rel="stylesheet" href="https://fonts.googleapis.com/css2?family=Arimo:wght@700&display=swap">
<style>
  :root {
    --stage: #dcdcdc;
    --ink: #111111;
    --paper: #ffffff;
    --night: #000000;
    --brand-blue: #1668b8;
    --tone-yellow: #f8bd1b;
    --tone-green: #2ba10e;
    --tone-blue: #1d80cc;
    --tone-blue-deep: #0a5aab;
    --icon-blue: #2b6cc4;
  }
  * { margin: 0; padding: 0; box-sizing: border-box; }
  html, body { width: 1200px; height: 785px; overflow: hidden; }
  body {
    background: var(--stage);
    font-family: "Arimo", Arial, sans-serif;
    font-weight: 700;
    position: relative;
  }
  .card {
    position: absolute;
    overflow: hidden;
    background: var(--paper);
  }
  .card--rounded { border-radius: 30px; }
  .card--back-dark { left: 188px; top: 94px; width: 422px; height: 263px; background: var(--night); }
  .card--front-rounded { left: 637px; top: 94px; width: 422px; height: 263px; }
  .card--back-light { left: 188px; top: 388px; width: 435px; height: 264px; }
  .card--front-square { left: 637px; top: 388px; width: 436px; height: 264px; }

  .wordmark {
    position: absolute;
    display: flex;
    align-items: center;
    gap: 12px;
    line-height: 1;
    color: var(--ink);
    letter-spacing: -0.5px;
  }
  .wordmark__square { background: var(--brand-blue); }

  .wordmark--large { font-size: 60px; }
  .wordmark--large .wordmark__square { width: 46px; height: 46px; }
  .card--back-dark .wordmark { left: 36px; top: 162px; color: var(--paper); }
  .card--back-light .wordmark { left: 38px; top: 178px; }

  .wordmark--small { font-size: 40px; }
  .wordmark--small .wordmark__square { width: 28px; height: 28px; }
  .card--front-rounded .wordmark { left: 26px; top: 86px; }
  .card--front-square .wordmark { left: 28px; top: 79px; }

  .contact {
    position: absolute;
    right: 30px;
    top: 46px;
    text-align: right;
    color: var(--ink);
  }
  .card--front-square .contact { top: 44px; }
  .contact__name { font-size: 15px; margin-bottom: 19px; }
  .contact__line {
    font-size: 10.5px;
    line-height: 14px;
    display: flex;
    justify-content: flex-end;
    align-items: center;
    gap: 3px;
  }
  .contact__icon { width: 8px; height: 8px; }
  .contact__line--plain { padding-right: 11px; }

  .tone-band {
    position: absolute;
    left: 0;
    right: 0;
    top: 160px;
    bottom: 0;
    background: linear-gradient(180deg,
      var(--tone-yellow) 0%,
      var(--tone-green) 22%,
      var(--tone-blue) 45%,
      var(--tone-blue-deep) 100%);
  }
</style>
</head>
<body>

  <section class="card card--rounded card--back-dark">
    <div class="wordmark wordmark--large"><span class="wordmark__square"></span>Vizo</div>
  </section>

  <section class="card card--rounded card--front-rounded">
    <div class="tone-band" role="img" aria-label="Layered flowing bands in yellow, green and blue across the lower card"></div>
    <div class="wordmark wordmark--small"><span class="wordmark__square"></span>Vizo</div>
    <div class="contact">
      <p class="contact__name">Marcus Delane</p>
      <p class="contact__line contact__line--plain">PO Box 415</p>
      <p class="contact__line contact__line--plain">Karratha Bay WA 6814</p>
      <p class="contact__line">+0400 123 456
        <svg class="contact__icon" viewBox="0 0 10 10" aria-hidden="true"><path d="M2 1 L4 3 L3 4 Q4 6 6 7 L7 6 L9 8 L8 9 Q3 9 1 2Z" fill="var(--icon-blue)"/></svg></p>
      <p class="contact__line">marcus@vizo.com.au
        <svg class="contact__icon" viewBox="0 0 10 10" aria-hidden="true"><rect x="1" y="2.5" width="8" height="5.5" fill="none" stroke="var(--icon-blue)" stroke-width="1.2"/><path d="M1 2.5 L5 6 L9 2.5" fill="none" stroke="var(--icon-blue)" stroke-width="1.2"/></svg></p>
      <p class="contact__line">www.vizo.com.au
        <svg class="contact__icon" viewBox="0 0 10 10" aria-hidden="true"><circle cx="5" cy="5" r="4" fill="none" stroke="var(--icon-blue)" stroke-width="1"/><path d="M1 5 H9 M5 1 V9" stroke="var(--icon-blue)" stroke-width="0.8"/></svg></p>
    </div>
  </section>

  <section class="card card--back-light">
    <div class="wordmark wordmark--large"><span class="wordmark__square"></span>Vizo</div>
  </section>

  <section class="card card--front-square">
    <div class="tone-band" role="img" aria-label="Layered flowing bands in yellow, green and blue across the lower card"></div>
    <div class="wordmark wordmark--small"><span class="wordmark__square"></span>Vizo</div>
    <div class="contact">
      <p class="contact__name">Marcus Delane</p>
      <p class="contact__line contact__line--plain">PO Box 415</p>
      <p class="contact__line contact__line--plain">Karratha Bay WA 6814</p>
      <p class="contact__line">+0400 123 456
        <svg class="contact__icon" viewBox="0 0 10 10" aria-hidden="true"><path d="M2 1 L4 3 L3 4 Q4 6 6 7 L7 6 L9 8 L8 9 Q3 9 1 2Z" fill="var(--icon-blue)"/></svg></p>
      <p class="contact__line">marcus@vizo.com.au
        <svg class="contact__icon" viewBox="0 0 10 10" aria-hidden="true"><rect x="1" y="2.5" width="8" height="5.5" fill="none" stroke="var(--icon-blue)" stroke-width="1.2"/><path d="M1 2.5 L5 6 L9 2.5" fill="none" stroke="var(--icon-blue)" stroke-width="1.2"/></svg></p>
      <p class="contact__line">www.vizo.com.au
        <svg class="contact__icon" viewBox="0 0 10 10" aria-hidden="true"><circle cx="5" cy="5" r="4" fill="none" stroke="var(--icon-blue)" stroke-width="1"/><path d="M1 5 H9 M5 1 V9" stroke="var(--icon-blue)" stroke-width="0.8"/></svg></p>
    </div>
  </section>

</body>
</html>
```